Meadowlark Recovery Brochure

We need a brochure template we can change photo's and words at a later date. WE offer rehabilitation to injured horses and ponies.
Either use our Meadowlark Grounds or Meadowlark Recovery logo but not both. A strong preference for the horse being led to feature first.

Target Market(s)

Horse Owners

Font styles to use
Serif

Colors
f78f20

Requirements
Must have
• Ability to write the text and interchange photos within the layout at a later date.
Nice to have
• Our colours are orange and black

```html
<!DOCTYPE html>
<html lang="en">
<head>
<meta charset="utf-8">
<title>Meadowlark Recovery – A Ray of Hope Brochure</title>
<link href="https://fonts.googleapis.com/css2?family=Cinzel:wght@400;500&family=Pinyon+Script&family=Arimo:wght@400&family=Montserrat:wght@800&display=swap" rel="stylesheet">
<style>
  :root {
    --cream: #fbf6c2;
    --peach: #f9cf8c;
    --orange: #f5955a;
    --brand-orange: #f07d2c;
    --hope-red: #e8432f;
    --ink: #1c1410;
    --band: #2b1713;
    --rule: #2a1e18;
    --white: #ffffff;
  }
  * { margin: 0; padding: 0; box-sizing: border-box; }
  html, body { width: 1200px; height: 849px; overflow: hidden; background: #ffffff; }
  .brochure {
    position: relative;
    width: 1200px; height: 849px;
    background: linear-gradient(180deg, var(--cream) 0%, var(--cream) 22%, var(--peach) 55%, var(--orange) 100%);
    font-family: "Arimo", Arial, sans-serif;
    color: var(--ink);
    overflow: hidden;
  }
  .panel-divider { position: absolute; top: 0; width: 1px; height: 849px; background: rgba(255,255,255,0.6); }
  .section-title {
    position: absolute;
    font-family: "Cinzel", Georgia, serif;
    font-weight: 400;
    font-size: 21px;
    letter-spacing: 1px;
    color: var(--ink);
    white-space: nowrap;
  }
  .section-title small { font-size: 16px; }
  .photo { position: absolute; }
  .photo-big-grey { left: 56px; top: 84px; width: 343px; height: 201px; background: linear-gradient(180deg, #a9c3d6 0%, #8f8a76 35%, #6f6555 100%); }
  .photo-herd { left: 400px; top: 84px; width: 350px; height: 202px; background: linear-gradient(180deg, #dfe3e4 0%, #b88a5c 40%, #6f9a4a 75%, #5f8f3d 100%); }
  .photo-sunny { left: 56px; top: 465px; width: 343px; height: 200px; background: linear-gradient(180deg, #8b8d84 0%, #9f7462 45%, #a89a8a 100%); }
  .body-copy {
    position: absolute;
    font-size: 12px;
    line-height: 17px;
    text-align: justify;
  }
  .contact-rule { position: absolute; left: 438px; top: 469px; width: 318px; height: 1.5px; background: var(--rule); }
  .brand { position: absolute; display: flex; align-items: center; gap: 8px; font-family: "Cinzel", Georgia, serif; font-weight: 500; white-space: nowrap; }
  .brand-contact { left: 453px; top: 503px; font-size: 24px; color: var(--ink); }
  .brand-contact .brand-mark { width: 42px; height: 74px; background: var(--ink); }
  .brand-cover { left: 913px; top: 43px; font-size: 30px; color: var(--brand-orange); }
  .brand-cover .brand-mark { width: 60px; height: 105px; background: var(--brand-orange); }
  .brand-name { line-height: 1.1; }
  .contact-list { position: absolute; left: 438px; top: 593px; list-style: none; }
  .contact-list li { display: flex; align-items: center; gap: 10px; height: 34px; font-size: 17px; white-space: nowrap; }
  .contact-list svg { width: 20px; height: 20px; flex: none; }
  .lower-band { position: absolute; left: 0; top: 0; }
  .herd-art { position: absolute; left: 418px; top: 735px; width: 372px; height: 82px; background: linear-gradient(90deg, rgba(150,80,50,0.35), rgba(170,90,55,0.55)); border-bottom: 2px solid #8fbf3c; }
  .tagline-script { position: absolute; left: 866px; top: 300px; font-family: "Pinyon Script", cursive; font-size: 62px; color: var(--band); white-space: nowrap; }
  .tagline-hope { position: absolute; left: 860px; top: 358px; font-family: "Montserrat", Arial, sans-serif; font-weight: 800; font-size: 92px; line-height: 1; color: var(--hope-red); letter-spacing: 1px; }
  .sunset-art { position: absolute; left: 801px; top: 530px; width: 399px; height: 319px;
    background: linear-gradient(180deg, rgba(247,160,95,0) 0%, #f6a262 35%, #9a4f2c 62%, var(--band) 85%, var(--band) 100%); }
  .website { position: absolute; left: 824px; top: 812px; font-family: "Arimo", Arial, sans-serif; font-size: 16px; color: var(--white); }
</style>
</head>
<body>
<main class="brochure">

  <h2 class="section-title" style="left:58px; top:52px;">BIG GREY – SPONSORED</h2>
  <div class="photo photo-big-grey" role="img" aria-label="Photo of two thin grey fillies standing in dry scrubland"></div>
  <p class="body-copy" style="left:56px; top:297px; width:304px;">One of two grey fillies saved by the AWRU from the ‘Kestrel’ case where 20+ horses starved to death in early 2016. Rehabilitated at MRC – Big Grey is now in training with Dana Pryor. Big Grey will need an experienced rider but she is beautiful. Big Grey is 16hh and rising 4.</p>

  <h2 class="section-title" style="left:57px; top:433px;">SUNNY – <small>TRAINING COMMENCED</small></h2>
  <div class="photo photo-sunny" role="img" aria-label="Photo of a chestnut pony in a rug with a bandaged leg, tied at a yard fence"></div>
  <p class="body-copy" style="left:56px; top:680px; width:318px;">Wow Sunny is now a stunning horse. Rescued by the AWRU as part of the Kestrel seizure – he is now in training with Tom Hartley. This stunning little horse is approx 4 yrs old and just 15 hh.</p>

  <div class="panel-divider" style="left:400px;"></div>

  <h2 class="section-title" style="right:450px; top:52px;">THE WILLOWBEND 16</h2>
  <div class="photo photo-herd" role="img" aria-label="Photo of a small herd of shaggy ponies walking across green pasture"></div>
  <p class="body-copy" style="left:443px; top:297px; width:307px;">Dumped on a country road near Willowbend – a little herd of 16! They quickly became the Willowbend 16. A little black stallion, a colt and 14 various mares and fillies. ALL unhandled and most mares in foal of course! We are slowly rehabilitating and educating these cute little guys.</p>

  <h2 class="section-title" style="left:439px; top:437px;">CONTACT</h2>
  <div class="contact-rule"></div>

  <div class="brand brand-contact">
    <span class="brand-name">Meadowlark<br>Recovery</span>
    <span class="brand-mark"></span>
  </div>

  <ul class="contact-list">
    <li><svg viewBox="0 0 20 20"><circle cx="10" cy="10" r="10" fill="#1c1410"/><path d="M10 4.5a3.5 3.5 0 0 0-3.5 3.5c0 2.6 3.5 7 3.5 7s3.5-4.4 3.5-7A3.5 3.5 0 0 0 10 4.5z" fill="#f5955a"/><circle cx="10" cy="8" r="1.3" fill="#1c1410"/></svg>Ferncliff VIC 3999</li>
    <li><svg viewBox="0 0 20 20"><circle cx="10" cy="10" r="10" fill="#1c1410"/><path d="M7 5l2 2.5-1.2 1.4a7 7 0 0 0 3.3 3.3l1.4-1.2L15 13l-1.2 1.6c-4 .2-8.6-4.4-8.4-8.4z" fill="#f5955a"/></svg>Phone: 0400 218 576</li>
    <li><svg viewBox="0 0 20 20"><circle cx="10" cy="10" r="10" fill="#1c1410"/><rect x="5" y="6.5" width="10" height="7" fill="#f5955a"/><path d="M5 6.5l5 4 5-4" stroke="#1c1410" stroke-width="1" fill="none"/></svg>E-mail: admin@meadowlarkrc.org.au</li>
  </ul>

  <svg class="lower-band" width="800" height="849" viewBox="0 0 800 849" aria-hidden="true">
    <polygon points="0,773 800,712 800,849 0,849" fill="var(--band)"/>
  </svg>
  <div class="herd-art" role="img" aria-label="Illustration of a mare, yearlings and a resting foal in silhouette"></div>

  <div class="panel-divider" style="left:800px;"></div>

  <div class="brand brand-cover">
    <span class="brand-name">Meadowlark<br>Recovery</span>
    <span class="brand-mark"></span>
  </div>

  <p class="tagline-script">A Ray of</p>
  <p class="tagline-hope">HOPE</p>

  <div class="sunset-art" role="img" aria-label="Illustration of two horse silhouettes on a hilltop against a setting sun"></div>
  <p class="website">www.meadowlarkrc.org.au</p>

</main>
</body>
</html>
```